New Cannabis Brand Velvet Ember needs exciting packaging.

We are looking for eye catching cannabis packaging for Flower products. There will be various strains so we need something that will fit into the entire Flower category. Our cannabis products are also all organic. We are hoping for unique, clean, something to pop out to customers in this crazy business. I have attached the Logo in the files. Coloring is optional if you want to follow the yellow and grey or just go on your own and come up with something unique. I have uploaded a file that shows a similar style package we are looking for with a small window to showcase the product? I need a space for a warning label, nutrition facts, ingredients, brand logo and then individualized item details. I plan on printing the design on custom mylar bags approx 4 x 6 inches to 5 x 6.5 inches. I will have other products in the line that may be packaged differently, but whichever designs are selected will likely be contracted for additional work to ensure consistency in branding. We are located in Arizona

Target Market(s)

Adult 21+

Industry/Entity Type

Cannabis

Font styles to use
Serif
Sans Serif
Script

Requirements
Must have
• small window in front for view of product.

```html
<!DOCTYPE html>
<html lang="en">
<head>
<meta charset="utf-8">
<title>Velvet Ember – Cannabis Flower Pouch</title>
<link rel="stylesheet" href="https://fonts.googleapis.com/css2?family=Kaushan+Script&family=Montserrat:wght@500;700;800&display=swap">
<style>
  :root {
    --backdrop: #b9c3c6;
    --pouch-black: #141414;
    --leaf-green: #2fb341;
    --leaf-green-dark: #1f7f2c;
    --silver: #eef0f0;
    --silver-shade: #d5d9da;
    --gold: #f2c51c;
    --gold-deep: #c9a227;
    --bud-tone: #8a7a5c;
    --bud-dark: #4e4534;
    --label-green: #2fb341;
    --text-light: #f4f4f4;
  }
  * { margin: 0; padding: 0; box-sizing: border-box; }
  html, body { width: 1200px; height: 674px; overflow: hidden; }
  body {
    background: var(--backdrop);
    font-family: "Montserrat", Arial, sans-serif;
    display: flex;
    align-items: center;
    justify-content: center;
  }
  .pouch {
    position: relative;
    width: 420px;
    height: 620px;
    background: var(--pouch-black);
    border-radius: 10px;
    overflow: hidden;
  }
  .leaf-pattern {
    position: absolute;
    inset: 0;
    background:
      radial-gradient(ellipse at 20% 30%, var(--leaf-green) 0 35%, transparent 60%),
      radial-gradient(ellipse at 80% 60%, var(--leaf-green) 0 30%, transparent 60%),
      linear-gradient(160deg, var(--leaf-green) 0%, var(--leaf-green-dark) 55%, var(--pouch-black) 100%);
  }
  .age-badge {
    position: absolute;
    top: 16px; left: 16px;
    width: 58px; height: 58px;
    border-radius: 50%;
    background: #2b2b2b;
    color: var(--text-light);
    font-weight: 800;
    font-size: 20px;
    display: flex; align-items: center; justify-content: center;
  }
  .brand-panel {
    position: absolute;
    top: 0; left: 96px;
    width: 228px; height: 142px;
    background: linear-gradient(180deg, var(--silver), var(--silver-shade));
    display: flex; flex-direction: column; align-items: center; justify-content: center;
    gap: 10px;
  }
  .brand-dot {
    width: 30px; height: 30px;
    border-radius: 50%;
    border: 2px solid var(--gold-deep);
  }
  .brand-name {
    color: var(--gold-deep);
    font-weight: 700;
    font-size: 17px;
    letter-spacing: 2px;
    text-transform: uppercase;
  }
  .product-title {
    position: absolute;
    top: 132px; left: 0; right: 0;
    text-align: center;
    font-family: "Kaushan Script", "Brush Script MT", cursive;
    color: var(--gold);
    line-height: 0.95;
    text-shadow: 3px 3px 0 var(--pouch-black);
  }
  .product-title .line-one { display: block; font-size: 84px; }
  .product-title .line-two { display: block; font-size: 84px; }
  .product-window {
    position: absolute;
    top: 330px; left: 95px;
    width: 230px; height: 190px;
    border-radius: 50%;
    background: radial-gradient(circle at 40% 40%, var(--bud-tone), var(--bud-dark));
  }
  .strain-details {
    position: absolute;
    left: 22px; bottom: 58px;
    color: var(--text-light);
    font-weight: 700;
    font-size: 14px;
    line-height: 1.25;
  }
  .net-weight {
    position: absolute;
    left: 50%; bottom: 16px;
    transform: translateX(-50%);
    background: var(--label-green);
    color: var(--pouch-black);
    font-weight: 700;
    font-size: 14px;
    padding: 5px 16px;
  }
  .compliance-badge {
    position: absolute;
    right: 22px; bottom: 26px;
  }
</style>
</head>
<body>
  <main class="pouch">
    <div class="leaf-pattern" role="img" aria-label="Green and black leaf pattern covering the pouch"></div>
    <div class="age-badge">21+</div>
    <div class="brand-panel">
      <span class="brand-dot"></span>
      <span class="brand-name">Velvet Ember</span>
    </div>
    <h1 class="product-title">
      <span class="line-one">Cannabis</span>
      <span class="line-two">Flower</span>
    </h1>
    <div class="product-window" role="img" aria-label="Clear window showing cannabis flower buds"></div>
    <p class="strain-details">Sour Diesel<br>THC 250 mg/g<br>CBD 0.08 mg/g</p>
    <div class="net-weight">Net Wt 0.5oz</div>
    <svg class="compliance-badge" width="52" height="52" viewBox="0 0 52 52" aria-hidden="true">
      <circle cx="26" cy="26" r="23" fill="#ffffff" stroke="#141414" stroke-width="3"/>
    </svg>
  </main>
</body>
</html>
```